Garnett and Lyle Personal Injury Billboard

We'd like a clean/modern billboard to build brand awareness for our law firm in the area of personal injury. Ideally, we like the word "Injured?" or something similar in large lettering.

I'm attaching images, logo and award badges which could be used. The billboards will be 14x48 ft and 10.6x36.

We are open to different color ideas, fonts, and artwork. Creative but not too busy with wording. Our web page is www.kgarnettfirm.example

Garnett & Lyle Law Firm
(555) 318-4092

```html
<!DOCTYPE html>
<html lang="en">
<head>
<meta charset="utf-8">
<title>Garnett &amp; Lyle Law Firm – Injured? Billboard</title>
<link rel="stylesheet" href="https://fonts.googleapis.com/css2?family=Anton&family=Montserrat:wght@600;700;800&display=swap">
<style>
  :root {
    --bg: #9a9a9a;
    --white: #ffffff;
    --ink: #1c1c1c;
    --red: #e00000;
    --blue: #1a9be0;
    --badge-dark: #222a36;
  }
  html, body {
    margin: 0;
    padding: 0;
    width: 1196px;
    height: 1200px;
    overflow: hidden;
    background: var(--bg);
  }
  .billboard {
    position: absolute;
    left: 48px;
    top: 440px;
    width: 1100px;
    height: 321px;
    background: var(--ink);
    box-shadow: 0 8px 14px rgba(0,0,0,0.35);
    font-family: "Montserrat", Arial, sans-serif;
    overflow: hidden;
  }
  .top-band {
    position: absolute;
    left: 0; top: 0;
    width: 100%;
    height: 160px;
    background: var(--white);
  }
  .firm-name {
    position: absolute;
    left: 34px;
    top: 44px;
    font-weight: 800;
    font-size: 27px;
    line-height: 32px;
    letter-spacing: 0.5px;
    color: var(--ink);
    white-space: nowrap;
  }
  .headline {
    position: absolute;
    left: 269px;
    top: 30px;
    margin: 0;
    font-family: "Anton", Impact, sans-serif;
    font-weight: 400;
    font-size: 128px;
    line-height: 1;
    color: var(--red);
    transform: scaleX(1.26);
    transform-origin: left top;
    white-space: nowrap;
  }
  .firm-stack {
    position: absolute;
    left: 37px;
    top: 184px;
    font-weight: 700;
    font-size: 32px;
    line-height: 37px;
    text-transform: uppercase;
    white-space: nowrap;
  }
  .firm-stack .accent { color: var(--blue); }
  .firm-stack .plain { color: var(--white); }
  .phone-icon {
    position: absolute;
    left: 257px;
    top: 183px;
    width: 53px;
    height: 53px;
  }
  .phone-number {
    position: absolute;
    left: 333px;
    top: 168px;
    font-weight: 700;
    font-size: 64px;
    line-height: 1;
    color: var(--white);
    white-space: nowrap;
  }
  .web-address {
    position: absolute;
    left: 250px;
    top: 246px;
    font-weight: 700;
    font-size: 38px;
    line-height: 1;
    color: var(--blue);
    white-space: nowrap;
    letter-spacing: 0.5px;
  }
  .award-badge {
    position: absolute;
    left: 873px;
    top: 42px;
    width: 172px;
    height: 242px;
  }
</style>
</head>
<body>
  <div class="billboard">
    <div class="top-band"></div>

    <div class="firm-name">
      <div>GARNETT</div>
      <div>&amp; LYLE</div>
    </div>

    <h1 class="headline">INJURED?</h1>

    <div class="firm-stack">
      <div class="accent">Garnett</div>
      <div class="accent">&amp; Lyle</div>
      <div class="plain">Law Firm</div>
    </div>

    <svg class="phone-icon" viewBox="0 0 54 54" aria-hidden="true">
      <circle cx="27" cy="27" r="27" fill="var(--blue)"/>
      <path d="M19 14c1.5-1 3-.8 3.8.6l2.3 4c.7 1.2.4 2.5-.6 3.3l-1.6 1.3c1.2 2.7 3.3 4.9 6 6.2l1.4-1.5c.9-1 2.2-1.2 3.3-.5l4 2.4c1.3.8 1.5 2.4.5 3.7-1.6 2.2-3.9 3.2-6.3 2.4C23.6 35.5 18.2 30 16.4 22.2c-.6-2.8.5-6.2 2.6-8.2z" fill="var(--white)"/>
    </svg>

    <div class="phone-number">(555) 318-4092</div>
    <div class="web-address">www.kgarnettfirm.example</div>

    <svg class="award-badge" viewBox="0 0 172 242" role="img" aria-label="Community choice award winner badge">
      <rect x="2" y="2" width="168" height="238" fill="var(--badge-dark)" stroke="var(--blue)" stroke-width="4"/>
      <rect x="2" y="2" width="168" height="54" fill="var(--blue)"/>
      <rect x="2" y="200" width="168" height="40" fill="var(--blue)"/>
    </svg>
  </div>
</body>
</html>
```